Brightpath Orthodontics appointment card design

I need appointment cards/ business cards made. Front will be Logo, name, title, email, phone number and location (5274 Willowmere Pkwy, Ste 312, Concord, NC 28027) . the back should have an appointment card (name, time, date) and also 3 addresses listed with a check box so we can check to which location they are going.
Brent Pellman Orthodontics
- 6315 Harlow Avenue, Ste 104, Harrisburg, NC 28075
- 2947 Rosvale Court SW, Ste 500, Concord, NC 28025
- 7163 Fernbrook Corporate Parkway, Ste 404, Charlotte, NC 28277
Business card can be horizontal or vertical in Design.
I need to be able to edit it to update and add new employees

Requirements
Must have
• Front:
• - Logo
• - Name & Title (able to be edited)
• - phone (704-555-0148) & Email (need to be able to edit)
• - Address: 5274 Willowmere Pkwy, Ste 312
• Concord, NC 28027
• Back:
• Appointment Card design:
• - Name, time, Date
• - 3 locations w/ a check box so the patient knows where to go:
• Brent Pellman Orthodontics
• - 6315 Harlow Avenue, Ste 104, Harrisburg, NC 28075
• - 2947 Rosvale Court SW, Ste 500, Concord, NC 28025
• - 7163 Fernbrook Corporate Parkway, Ste 404, Charlotte, NC 28277

```html
<!DOCTYPE html>
<html lang="en">
<head>
<meta charset="utf-8">
<title>Brightpath Orthodontics – Business &amp; Appointment Card</title>
<link rel="stylesheet" href="https://fonts.googleapis.com/css2?family=Nunito:wght@600;700;800&display=swap">
<style>
  :root {
    --backdrop: #2185c4;
    --card: #ffffff;
    --brand-light: #1f8bc9;
    --brand-dark: #1563a6;
    --brand-text: #1b75bb;
    --ink-white: #ffffff;
    --label-grey: #a5a9b0;
    --rule-blue: #1b75bb;
  }
  html, body {
    margin: 0;
    padding: 0;
    width: 975px;
    height: 1200px;
    overflow: hidden;
    background: var(--backdrop);
    font-family: "Nunito", sans-serif;
  }
  .card {
    position: absolute;
    left: 126px;
    width: 726px;
    height: 414px;
    background: var(--card);
    overflow: hidden;
  }
  .card--front { top: 133px; }
  .card--back  { top: 634px; }

  .tab {
    position: absolute;
    top: 0;
    background: linear-gradient(90deg, var(--brand-light), var(--brand-dark));
    border-radius: 0 0 140px 140px;
    color: var(--ink-white);
  }

  /* Front */
  .front-wordmark {
    position: absolute;
    left: 52px;
    top: 168px;
    margin: 0;
    font-size: 32px;
    font-weight: 800;
    line-height: 1.1;
    color: var(--brand-text);
  }
  .tab--contact {
    left: 373px;
    width: 278px;
    height: 351px;
  }
  .person-name {
    position: absolute;
    left: 26px;
    top: 93px;
    margin: 0;
    font-size: 21px;
    font-weight: 700;
  }
  .person-title {
    position: absolute;
    left: 27px;
    top: 122px;
    margin: 0;
    font-size: 14px;
    font-weight: 600;
  }
  .contact-list {
    position: absolute;
    left: 22px;
    top: 170px;
    margin: 0;
    padding: 0;
    list-style: none;
  }
  .contact-item {
    position: relative;
    padding-left: 40px;
    font-size: 13.5px;
    font-weight: 600;
    line-height: 17px;
    margin-bottom: 16px;
  }
  .contact-item svg {
    position: absolute;
    left: 2px;
    top: 0;
    width: 20px;
    height: 20px;
    fill: var(--ink-white);
  }
  .contact-item--address { margin-top: -6px; }
  .contact-item--address svg { top: 2px; width: 22px; height: 22px; left: 1px; }

  /* Back */
  .tab--locations {
    left: 68px;
    width: 267px;
    height: 336px;
  }
  .section-title {
    position: absolute;
    margin: 0;
    padding: 3px 0;
    border-top: 1.5px solid currentColor;
    border-bottom: 1.5px solid currentColor;
    font-weight: 700;
    line-height: 1.2;
  }
  .tab--locations .section-title {
    left: 69px;
    top: 41px;
    font-size: 16px;
  }
  .location-list {
    position: absolute;
    left: 17px;
    top: 116px;
    margin: 0;
    padding: 0;
    list-style: none;
  }
  .location-item {
    position: relative;
    padding-left: 28px;
    font-size: 12.5px;
    font-weight: 700;
    line-height: 15.5px;
    margin-bottom: 17px;
  }
  .location-item:last-child { margin-top: 4px; }
  .checkbox {
    position: absolute;
    left: 0;
    top: 9px;
    width: 14px;
    height: 14px;
    background: var(--ink-white);
  }
  .appointment .section-title {
    left: 401px;
    top: 42px;
    font-size: 23px;
    color: var(--brand-text);
  }
  .field {
    position: absolute;
    left: 400px;
    width: 298px;
    border-bottom: 1.5px solid var(--rule-blue);
    font-size: 13.5px;
    font-weight: 600;
    color: var(--label-grey);
    line-height: 18px;
  }
  .field--name  { top: 124px; }
  .field--extra { top: 162px; height: 18px; }
  .field--time  { top: 203px; }
  .field--date  { top: 245px; }
  .back-wordmark {
    position: absolute;
    left: 406px;
    top: 308px;
    margin: 0;
    font-size: 21px;
    font-weight: 800;
    line-height: 1.1;
    color: var(--brand-text);
  }
</style>
</head>
<body>

<section class="card card--front" aria-label="Card front">
  <p class="front-wordmark">Brightpath<br>Orthodontics</p>

  <div class="tab tab--contact">
    <h1 class="person-name">Full Name</h1>
    <p class="person-title">job title</p>
    <ul class="contact-list">
      <li class="contact-item">
        <svg viewBox="0 0 24 24" aria-hidden="true"><path d="M6.6 10.8a15.1 15.1 0 0 0 6.6 6.6l2.2-2.2a1 1 0 0 1 1-.25 11.4 11.4 0 0 0 3.6.57 1 1 0 0 1 1 1V20a1 1 0 0 1-1 1A17 17 0 0 1 3 4a1 1 0 0 1 1-1h3.5a1 1 0 0 1 1 1c0 1.25.2 2.45.57 3.57a1 1 0 0 1-.25 1z"/></svg>
        704-555-0148
      </li>
      <li class="contact-item">
        <svg viewBox="0 0 24 24" aria-hidden="true"><path d="M2 5h20v14H2z M3.5 6.5 12 13l8.5-6.5" fill="none" stroke="#fff" stroke-width="1.8"/></svg>
        hello@brightpathortho.com
      </li>
      <li class="contact-item contact-item--address">
        <svg viewBox="0 0 24 24" aria-hidden="true"><path d="M12 2 1 12h3v10h6v-6h4v6h6V12h3z"/></svg>
        5274 Willowmere Pkwy,<br>Ste 312 Concord, NC 28027
      </li>
    </ul>
  </div>
</section>

<section class="card card--back" aria-label="Card back">
  <div class="tab tab--locations">
    <h2 class="section-title">OUR LOCATIONS</h2>
    <ul class="location-list">
      <li class="location-item"><span class="checkbox"></span>6315 Harlow Avenue, Ste 104,<br>Harrisburg, NC 28075</li>
      <li class="location-item"><span class="checkbox"></span>2947 Rosvale Court SW,<br>Ste 500, Concord, NC 28025</li>
      <li class="location-item"><span class="checkbox"></span>7163 Fernbrook Corporate Pkwy,<br>Ste 404, Charlotte, NC 28277</li>
    </ul>
  </div>

  <div class="appointment">
    <h2 class="section-title">APPOINTMENT</h2>
    <div class="field field--name">Full Name:</div>
    <div class="field field--extra"></div>
    <div class="field field--time">Time:</div>
    <div class="field field--date">Date:</div>
    <p class="back-wordmark">Brightpath<br>Orthodontics</p>
  </div>
</section>

</body>
</html>
```